Curtain and Blind Manufacturers - Retail Ecommerce All Pages

To Design a high converting website design for and improve on the domain www.velcourt-weaves.co.uk.

Generally it is improvements on what already exists, the core layout is functional and strong. Needs to have the header mobile responsive. Core elements for each page and clear content.

Current header is good just needs modernising and needs to work well on mobile. Need a way of having a mixture of categories and advice where necessary.

Pages and detailing required.
Home - Great Imagery for the sections. Category specific. A good product offering. So Call to product. Potentially straight to our best selling products. Not in a slider but in a straight forward grid. A nice simlar design to competitors in my space. shutterly4u, my own website. also i like websites like nessa mattresses, harrowdens.co.uk needs to be simple with clear direction for the customer particularly on mobile to get them to what we do quickly. EG curtains, blinds etc

Inner pages

Category Top Filters
https://www.velcourt-weaves.co.uk/flame-retardant/curtains

Category Side bar filters

Category Mobile with Off Canvas Filters

Product - Fabric
https://www.velcourt-weaves.co.uk/tovra-flame-retardant-curtain-fabric.html

Product - Curtains - https://www.velcourt-weaves.co.uk/tovra-fr-curtains.html

Product - Blinds
Cart
Checkout
Slide in Cart
Slide in Filters
General Content Page
About

```html
<!DOCTYPE html>
<html lang="en">
<head>
<meta charset="utf-8">
<title>Velcourt Weaves – Curtains, Blinds, Fabric</title>
<link rel="stylesheet" href="https://fonts.googleapis.com/css2?family=Poppins:wght@400;500;600;700&family=Montserrat:ital,wght@0,400;0,500;0,600;1,400&display=swap">
<style>
:root{
  --red:#d40a0a;
  --red-dark:#b80000;
  --pink:#f9dede;
  --ink:#1b1b1b;
  --muted:#7c7c7c;
  --line:#e4e4e4;
  --grey-bg:#f1f1f1;
  --white:#fff;
}
*{box-sizing:border-box;margin:0;padding:0}
html,body{width:1200px;height:3580px;overflow:hidden}
body{position:relative;background:var(--white);font-family:"Montserrat",sans-serif;color:var(--ink)}
.abs{position:absolute}
.btn{display:inline-flex;align-items:center;justify-content:center;border-radius:999px;font-family:"Poppins",sans-serif;font-weight:600;text-transform:uppercase}
.btn-red{background:var(--red);color:var(--white)}
.btn-ghost{border:1.5px solid var(--red);color:var(--red);background:var(--white)}

/* top bar */
.topbar{left:0;top:0;width:1200px;height:38px;background:var(--pink)}
.pay{display:flex;gap:5px;position:absolute;left:105px;top:10px}
.pay span{width:28px;height:18px;border-radius:2px;background:#c9cfdb}
.pay span:nth-child(1){background:#e7a23a}.pay span:nth-child(2){background:#2d4d9c}.pay span:nth-child(3){background:#2f84c9}.pay span:nth-child(4){background:#e9e9e9}
.callus{position:absolute;right:110px;top:6px;display:flex;align-items:center;gap:8px;font-family:"Poppins",sans-serif;font-size:11px;font-weight:500}
.ico-round{width:26px;height:26px;border-radius:50%;background:var(--red);display:flex;align-items:center;justify-content:center}

/* header */
.header{left:0;top:38px;width:1200px;height:70px}
.logo{position:absolute;display:flex;align-items:center;gap:8px;font-family:"Poppins",sans-serif;font-weight:700;color:var(--red);font-size:19px;letter-spacing:.5px}
.logo .mark{width:26px;height:26px;background:var(--red)}
.cart{left:498px;top:18px;width:36px;height:36px;border-radius:50%;background:var(--red);display:flex;align-items:center;justify-content:center}
.search{left:552px;top:17px;width:256px;height:38px;border:1.5px solid var(--red);border-radius:999px;display:flex;align-items:center;gap:10px;padding-left:14px;font-size:11px;color:#999}
.login{left:826px;top:17px;width:126px;height:38px;font-size:14px;font-weight:500}
.contact{left:959px;top:17px;width:144px;height:38px;font-size:14px;font-weight:500}

/* nav */
.nav{left:0;top:108px;width:1200px;height:50px;background:var(--red);display:flex;align-items:center;padding-left:134px;gap:0}
.nav a{color:var(--white);text-decoration:none;font-family:"Poppins",sans-serif;font-size:14px;font-weight:500;margin-right:30px}
.nav a:nth-child(5){margin-right:36px}.nav a:nth-child(8){margin-right:50px}

/* product grid */
.grid{left:164px;top:217px;display:grid;grid-template-columns:repeat(3,282px);column-gap:14px;row-gap:29px}
.tile{position:relative;width:282px;height:350px}
.tile .photo{width:282px;height:185px}
.tile .card{position:absolute;left:18px;top:158px;width:246px;height:190px;background:var(--white);box-shadow:0 3px 10px rgba(0,0,0,.09);padding:22px 18px 0 19px}
.card h3{font-family:"Poppins",sans-serif;font-size:14px;font-weight:600;line-height:1.3;text-transform:uppercase;height:40px}
.card h3.sentence{text-transform:none}
.card p{font-size:10.5px;color:var(--muted);line-height:1.55;margin-top:4px}
.card .btn{width:90px;height:23px;font-size:9px;margin-top:10px}

/* specialists */
.specialists{left:0;top:1388px;width:1200px;height:792px;background:var(--grey-bg)}
.specialists h2{position:absolute;left:0;top:52px;width:1200px;text-align:center;font-family:"Poppins",sans-serif;font-size:29px;font-weight:700;line-height:1.18}
.specialists .lead{position:absolute;left:125px;top:142px;width:950px;text-align:center;font-size:14px;line-height:1.84;color:#333}
.features{position:absolute;left:106px;top:312px;display:grid;grid-template-columns:repeat(3,300px);column-gap:43px}
.feature{background:var(--white);height:408px;box-shadow:0 2px 8px rgba(0,0,0,.06)}
.feature .photo{height:177px}
.feature .body{padding:24px 26px 0}
.feature h3{font-family:"Poppins",sans-serif;font-size:18px;font-weight:500;text-transform:uppercase}
.feature p{font-size:12.5px;color:var(--muted);line-height:1.36;margin-top:10px}
.feature .btn{width:102px;height:27px;font-size:10px;margin-top:12px;font-weight:500}

/* about */
.about-photo{left:138px;top:2256px;width:424px;height:424px;border-radius:50%;border:6px solid var(--red);border-right-color:transparent;border-bottom-color:transparent;transform:rotate(-20deg);padding:8px}
.about-photo .photo{width:100%;height:100%;border-radius:50%;transform:rotate(20deg)}
.about-text{left:626px;top:2290px;width:440px}
.about-text h2{font-family:"Poppins",sans-serif;font-size:28px;font-weight:700;color:var(--red);line-height:1.22}
.about-text p{font-size:14px;line-height:1.36;color:#333;margin-top:16px}
.about-text .btn{width:154px;height:41px;font-size:16px;margin-top:18px;font-weight:500}

/* testimonials */
.reviews{left:39px;top:2775px;display:grid;grid-template-columns:repeat(3,354px);column-gap:30px}
.review{height:170px;background:var(--white);box-shadow:0 2px 12px rgba(0,0,0,.09);padding:34px 26px 0 26px;position:relative}
.review .q{position:absolute;font-family:"Poppins",sans-serif;font-size:38px;color:#ccc;line-height:1}
.review p{font-style:italic;font-size:10px;line-height:1.85;color:var(--muted);padding-left:28px}
.author{display:flex;align-items:center;gap:10px;margin-top:14px;padding-left:10px}
.avatar{width:34px;height:34px;border-radius:50%;background:#e6d2bf}
.author b{font-size:11px;font-weight:500;display:block}
.author small{font-size:9.5px;color:#999}
.dots{left:568px;top:2976px;display:flex;gap:7px}
.dots i{width:11px;height:11px;border-radius:50%;background:var(--red);display:block}
.dots i:first-child{background:var(--white);border:1.5px solid var(--red)}

/* footer */
.footer{left:0;top:3053px;width:1200px;height:527px;background:linear-gradient(180deg,#d60707,#c90303);color:var(--white)}
.footer .logo{color:var(--white);left:107px;top:80px}
.footer .logo .mark{background:var(--white)}
.fpay{position:absolute;left:110px;top:145px;display:flex;gap:10px}
.fpay span{width:28px;height:17px;background:rgba(255,255,255,.85);border-radius:2px}
.newsletter h2{position:absolute;left:424px;top:68px;font-family:"Poppins",sans-serif;font-size:24px;font-weight:700}
.news-form{position:absolute;left:424px;top:112px;width:638px;height:48px;background:var(--white);display:flex;align-items:center;padding:4px}
.news-form span{flex:1;padding-left:9px;font-size:11px;color:#777}
.news-form b{width:140px;height:40px;background:var(--red);display:flex;align-items:center;justify-content:center;font-family:"Poppins",sans-serif;font-size:12.5px;font-weight:600}
.fcol{position:absolute;top:196px}
.fcol h4{font-family:"Poppins",sans-serif;font-size:14px;font-weight:500;text-decoration:underline;text-underline-offset:4px;margin-bottom:14px}
.fcol li{list-style:none;font-size:12px;line-height:26.4px}
.contact-item{display:flex;gap:10px;font-size:12px;line-height:1.5;margin-bottom:14px}
.contact-item .ico-round{width:30px;height:30px;background:var(--white);flex:none}
.social{display:flex;gap:4px}
.social span{width:28px;height:28px;border-radius:50%;border:1.5px solid var(--white)}
.fbottom{position:absolute;left:0;top:462px;width:1200px;border-top:1px solid rgba(255,255,255,.4);text-align:center;padding-top:26px;font-size:11px}
</style>
</head>
<body>

<div class="abs topbar">
  <div class="pay"><span></span><span></span><span></span><span></span></div>
  <div class="callus">
    <div class="ico-round"><svg width="13" height="13" viewBox="0 0 24 24"><path fill="#fff" d="M6.6 10.8a15 15 0 0 0 6.6 6.6l2.2-2.2a1 1 0 0 1 1-.25 11.4 11.4 0 0 0 3.6.6 1 1 0 0 1 1 1V20a1 1 0 0 1-1 1A17 17 0 0 1 3 4a1 1 0 0 1 1-1h3.5a1 1 0 0 1 1 1c0 1.25.2 2.45.6 3.6a1 1 0 0 1-.25 1z"/></svg></div>
    <span>Call Us Today&nbsp; 0117 4960 218</span>
  </div>
</div>

<header class="abs header">
  <div class="logo" style="left:105px;top:17px"><span class="mark"></span>VELCOURT WEAVES</div>
  <div class="abs cart"><svg width="17" height="17" viewBox="0 0 24 24" fill="none" stroke="#fff" stroke-width="2"><path d="M3 4h2l2.4 11h10.2l2-8H6.3"/><circle cx="9" cy="19" r="1.4"/><circle cx="17" cy="19" r="1.4"/></svg></div>
  <div class="abs search"><svg width="14" height="14" viewBox="0 0 24 24" fill="none" stroke="#d40a0a" stroke-width="2.6"><circle cx="10" cy="10" r="6.5"/><path d="M15 15l5 5"/></svg>Search here</div>
  <div class="abs btn btn-red login">LOGIN</div>
  <div class="abs btn btn-ghost contact">CONTACT US</div>
</header>

<nav class="abs nav">
  <a>HOME</a><a>CURTAINS</a><a>BLINDS</a><a>FABRICS</a><a>FLAME RETARDANT</a><a>TRACKS</a><a>PLOES</a><a>BEDDING &amp; LINENS</a><a>FURNITURE</a>
</nav>

<section class="abs grid">
  <article class="tile"><div class="photo" role="img" aria-label="Bedroom with yellow striped flame retardant curtains" style="background:linear-gradient(90deg,#cfc8b8,#c4a640 45%,#ddd8cc)"></div>
    <div class="card"><h3>Flame Retardant Curtains</h3><p>Vivamus porttitor purus nisi eleifend libero a tempus libero lectus feugiat felis Morbi diam mauris viverra in gra</p><span class="btn btn-red">Read More</span></div></article>
  <article class="tile"><div class="photo" role="img" aria-label="Stage with purple theatre curtains" style="background:linear-gradient(135deg,#2a1a4a,#6a2fb0 50%,#1c1330)"></div>
    <div class="card"><h3>Stage / Theatre Curtains</h3><p>Vivamus porttitor purus nisi eleifend libero a tempus libero lectus feugiat felis Morbi diam mauris viverra in gra</p><span class="btn btn-red">Read More</span></div></article>
  <article class="tile"><div class="photo" role="img" aria-label="White flame retardant bedding" style="background:linear-gradient(135deg,#cfcfcf,#f2f2f2 60%,#dadada)"></div>
    <div class="card"><h3>Flame Retardant Bedding</h3><p>Vivamus porttitor purus nisi eleifend libero a tempus libero lectus feugiat felis Morbi diam mauris viverra in gra</p><span class="btn btn-red">Read More</span></div></article>

  <article class="tile"><div class="photo" role="img" aria-label="Rolls of coloured fire resistant curtain fabric" style="background:linear-gradient(120deg,#c07a3a,#5b9fb3 40%,#4a5c6b 70%,#2c2c2c)"></div>
    <div class="card"><h3>Fire Resistant Curtain Fabrics</h3><p>Vivamus porttitor purus nisi eleifend libero a tempus libero lectus feugiat felis Morbi diam mauris viverra in gra</p><span class="btn btn-red">Read More</span></div></article>
  <article class="tile"><div class="photo" role="img" aria-label="Lime green fire retardant roller blind" style="background:linear-gradient(90deg,#c3cd5a,#b2bd3e 70%,#e8e8e8)"></div>
    <div class="card"><h3>Fire Retardant Roller Blinds</h3><p>Vivamus porttitor purus nisi eleifend libero a tempus libero lectus feugiat felis Morbi diam mauris viverra in gra</p><span class="btn btn-red">Read More</span></div></article>
  <article class="tile"><div class="photo" role="img" aria-label="Blue cubicle curtain on a ceiling track" style="background:linear-gradient(180deg,#dcdcdc,#9fbad9 50%,#7f9fc7)"></div>
    <div class="card"><h3>Cubicle Curtains and Tracks</h3><p>Vivamus porttitor purus nisi eleifend libero a tempus libero lectus feugiat felis Morbi diam mauris viverra in gra</p><span class="btn btn-red">Read More</span></div></article>

  <article class="tile"><div class="photo" role="img" aria-label="White aluminium curtain track on black" style="background:linear-gradient(160deg,#111,#2b2b2b 50%,#0c0c0c)"></div>
    <div class="card"><h3 class="sentence">Curtain Tracks</h3><p>Vivamus porttitor purus nisi eleifend libero a tempus libero lectus feugiat felis Morbi diam mauris viverra in gra</p><span class="btn btn-red">Read More</span></div></article>
  <article class="tile"><div class="photo" role="img" aria-label="Blue metal venetian blinds" style="background:linear-gradient(90deg,#1f3f9a,#3f6bd1 45%,#2a3f7a)"></div>
    <div class="card"><h3 class="sentence">Metal Venetian Blinds</h3><p>Vivamus porttitor purus nisi eleifend libero a tempus libero lectus feugiat felis Morbi diam mauris viverra in gra</p><span class="btn btn-red">Read More</span></div></article>
  <article class="tile"><div class="photo" role="img" aria-label="Burgundy vertical blinds" style="background:linear-gradient(90deg,#8c2d52,#a9466d 50%,#7a2447)"></div>
    <div class="card"><h3 class="sentence">Vertical Blinds</h3><p>Vivamus porttitor purus nisi eleifend libero a tempus libero lectus feugiat felis Morbi diam mauris viverra in gra</p><span class="btn btn-red">Read More</span></div></article>
</section>

<section class="abs specialists">
  <h2>Flame Retardant &amp; Contract<br>Furnishing Specialists</h2>
  <p class="lead">Velcourt Weaves supply the UK with soft furnishings for commercial environments certified to British and International Flame Retardant Standards . Including BS5867, BS7175, BS5852, IMO M1 &amp; B1. Velcourt Weaves has been set up to supply the UK and the world with a superior range of contract furnishings. From manufacture to installation. We are an NCS certified supplier and work supplying hotels, care homes, schools and more. Our company is based in the United Kingdom. We look forward to working with you to supply the very best contract curtains, blinds, stage curtains and also cubicle curtains and tracks.</p>
  <div class="features">
    <article class="feature"><div class="photo" role="img" aria-label="Sewing workshop with industrial machines" style="background:linear-gradient(135deg,#b7b0a4,#e3ded6 50%,#8f887e)"></div>
      <div class="body"><h3>UK Manufactured</h3><p>All our curtains and blinds are made here in the United Kingdom. We believe in quality and buying British where possible, so we make all of our made to measure soft furnishings including; curtains, blinds, accessories here in the UK.</p><span class="btn btn-ghost">Read More</span></div></article>
    <article class="feature"><div class="photo" role="img" aria-label="Healthcare certification badge" style="background:#1565c0"></div>
      <div class="body"><h3>NCS Certified Supplier</h3><p>Velcourt Weaves are registered NCS suppliers working on small projects for individual medical practices as well as full hospital contract for cubicle curtain rails</p><span class="btn btn-ghost">Read More</span></div></article>
    <article class="feature"><div class="photo" role="img" aria-label="Pale pink cassette roller blind" style="background:linear-gradient(180deg,#e9e6e4,#eecdcf 40%,#e7c3c6)"></div>
      <div class="body"><h3>Cassettte Roller Blinds</h3><p>A cassette blackout roller blind manufacturer who manufacturers the very best roller blinds for commercial and domestic situations. Our cassette roller blinds are of the highest quality and made to last with a 10 year guarentee. Speak with the team to get a quote for</p><span class="btn btn-ghost">Read More</span></div></article>
  </div>
</section>

<div class="abs about-photo"><div class="photo" role="img" aria-label="Bedroom with yellow striped curtains and a striped bedspread" style="background:radial-gradient(circle at 40% 40%,#e9e2cf,#c9a94a 55%,#8c7a55)"></div></div>
<section class="abs about-text">
  <h2>Velcourt Weaves - Curtains, Blinds, Fabric</h2>
  <p><b style="font-weight:600">Velcourt Weaves has been set up to supply the UK and the world with a superior range of curtain fabrics</b> and made to measure curtains. Ensuring that all products are certified to the necessary British and European flame retardant standards. Ourflame retardant fabrics are manufactured into excellent curtains, blinds and soft furnishings in our factories across the UK. Purchase your contract curtains and soft furnishings from a UK company with a large buying power that can offer the full service from design, manufacture and installation of contract furnishings. The team at Velcourt Weaves will ensure that you can get the project completed on time and on budget with made to measure curtains manufactured in as little as 15-20 working days.</p>
  <span class="btn btn-red">Read More</span>
</section>

<section class="abs reviews">
  <article class="review"><span class="q" style="left:24px;top:32px">“</span><p>Allamcorper est eget tempor cursus neque mi consectetuer mi a ultricies massa est sed nisl Class aptent taciti sociosqu ad litora torquent per conubia nostra per</p><span class="q" style="left:254px;top:76px">”</span>
    <div class="author"><span class="avatar"></span><div><b>By Author Name</b><small>Marketing Manager</small></div></div></article>
  <article class="review"><span class="q" style="left:24px;top:32px">“</span><p>Allamcorper est eget tempor cursus neque mi consectetuer mi a ultricies massa est sed nisl Class aptent taciti sociosqu ad litora torquent per conubia nostra per</p><span class="q" style="left:254px;top:76px">”</span>
    <div class="author"><span class="avatar"></span><div><b>By Author Name</b><small>Marketing Manager</small></div></div></article>
  <article class="review"><span class="q" style="left:24px;top:32px">“</span><p>Allamcorper est eget tempor cursus neque mi consectetuer mi a ultricies massa est sed nisl Class aptent taciti sociosqu ad litora torquent per conubia nostra per</p><span class="q" style="left:254px;top:76px">”</span>
    <div class="author"><span class="avatar"></span><div><b>By Author Name</b><small>Marketing Manager</small></div></div></article>
</section>
<div class="abs dots"><i></i><i></i><i></i><i></i></div>

<footer class="abs footer">
  <div class="logo"><span class="mark"></span>VELCOURT WEAVES</div>
  <div class="fpay"><span></span><span></span><span></span><span></span><span></span></div>
  <div class="newsletter"><h2>Suscribe a Newsletter</h2>
    <div class="news-form"><span>Suscribe a Newsletter</span><b>SUSCRIBE NOW</b></div></div>

  <div class="fcol" style="left:104px"><h4>NAVIGATION</h4><ul><li>Home</li><li>About Us</li><li>FAQ</li><li>Blog</li><li>Reviews</li><li>Charity</li><li>Contact Us</li></ul></div>
  <div class="fcol" style="left:247px"><h4>USEFUL LINKS</h4><ul><li>Privacy Policy</li><li>Terms and Conditions</li><li>Returns &amp; Cancellation</li><li>Delivery &amp; Shipping Information</li><li>Curtain and Blind Installation Nationwide</li><li>How to Measure for Curtains and Blinds</li></ul></div>
  <div class="fcol" style="left:531px"><h4>OUR PRODUCTS</h4><ul><li>Flame Retardant Curtains</li><li>Fire Resistant Blinds</li><li>Made to Measure Curtains</li><li>Acoustic Curtains</li><li>Curtain Fabrics</li><li>Curtain Poles</li><li>Curtain Tracks</li></ul></div>
  <div class="fcol" style="left:733px;top:193px"><h4>CONTACT US</h4>
    <div class="contact-item"><span class="ico-round"><svg width="14" height="14" viewBox="0 0 24 24"><path fill="#d40a0a" d="M6.6 10.8a15 15 0 0 0 6.6 6.6l2.2-2.2a1 1 0 0 1 1-.25 11.4 11.4 0 0 0 3.6.6 1 1 0 0 1 1 1V20a1 1 0 0 1-1 1A17 17 0 0 1 3 4a1 1 0 0 1 1-1h3.5a1 1 0 0 1 1 1c0 1.25.2 2.45.6 3.6a1 1 0 0 1-.25 1z"/></svg></span><div>Phone<br>123-456-7890</div></div>
    <div class="contact-item"><span class="ico-round"><svg width="14" height="14" viewBox="0 0 24 24" fill="none" stroke="#d40a0a" stroke-width="2"><rect x="3" y="5" width="18" height="14" rx="1"/><path d="M3 6l9 7 9-7"/></svg></span><div>Email<br>info@velcourt-weaves.co.uk</div></div>
    <div class="contact-item"><span class="ico-round"><svg width="14" height="14" viewBox="0 0 24 24"><path fill="#d40a0a" d="M12 2a7 7 0 0 0-7 7c0 5 7 13 7 13s7-8 7-13a7 7 0 0 0-7-7zm0 9.5A2.5 2.5 0 1 1 12 6.5a2.5 2.5 0 0 1 0 5z"/></svg></span><div>Address<br>27 Harrow Lane, Ells-<br>worth VIC 3104</div></div>
  </div>
  <div class="fcol" style="left:942px"><h4>FOLLOW US</h4><div class="social"><span></span><span></span><span></span><span></span></div></div>

  <div class="fbottom">© 2023 VELCOURT WEAVES. ALL RIGHTS RESERVED</div>
</footer>

</body>
</html>
```